Larkspur Site Services LLC

We need a professional and colorful website that describes our company [please see below]:

CORE COMPETENCIES

About Us: Larkspur Site Services, LLC is a veteran-owned business, and is a leading force in the construction industry. We have continuously provided exceptional services to our clients. With a wealth of experience and a commitment of excellence, we have earned a reputation for delivering high-quality projects on time and within budget.

Core Competencies:

Experience: With decades of experience, we bring unparalleled expertise to every project we undertake. Our team consists of seasoned professionals who are experts in their respective fields.

Portfolio: Our portfolio encompasses a wide range of construction projects, including commercial building, industrial facilities, infrastructure development and more.

Innovation: We stay at the forefront of industry trends and technologies, leveraging the latest tools and techniques to deliver innovative solutions.

Client Satisfaction: Our commitment to client satisfaction is unwavering. We prioritize open communication, transparency, and responsiveness, working closely with clients to understand their needs and deliver results.

Safety: Safety is our top priority on every job site. We adhere to the highest safety standards and implement rigorous safety protocols to ensure the well-being of our workers and stakeholders.

KEY SERVICES

General Contracting
Construction Management
Design-Build Services
Pre-construction Planning
Value Engineering
Sustainable Construction Practices
Renovation and Remodeling
Quality Assurance and Control
Project Estimating and Budgeting
Permitting and Regulatory Compliance

CONTACT INFORMATION

Dominic Harlowe, President
Email Address [TBD]
Website Address [TBD]
555.214.6730

Target Market(s)

Federal Government and Commercial Agencies

Industry/Entity Type

Construction and Design Build

Coding

Coded - Design and coding required

Number of Pages Required

2 page

Colors

Designer to choose colors to be used in the design.

Requirements
Must have
• Please use our attached logo and color scheme that was designed through Pixel Bazaar. Please include the Nation's Capitol building with a patriotic feel and include a diverse work force. Include federal buildings in the pictures. Please include in the opeing tagline that the company is Veteran Owned.

```html
<!DOCTYPE html>
<html lang="en">
<head>
<meta charset="utf-8">
<title>Larkspur Site Services LLC</title>
<link href="https://fonts.googleapis.com/css2?family=Varela+Round&display=swap" rel="stylesheet">
<style>
:root{
  --stage:#dddfe8;
  --navy:#262d66;
  --ink:#1f2447;
  --muted:#4d5a9a;
  --green:#8dc63f;
  --grey-bg:#f3f4f6;
  --line:#c9ccdc;
  --sky:#e0eaf4;
  --bubble:#8f98b8;
  --white:#ffffff;
  --bar:#f4f6f9;
}
*{box-sizing:border-box;margin:0;padding:0}
html,body{width:1200px;height:2384px;overflow:hidden}
body{background:var(--stage);font-family:"Varela Round",sans-serif;color:var(--ink)}
.page{position:absolute;left:287px;top:74px;width:626px;background:var(--white);box-shadow:6px 8px 24px rgba(40,45,90,.18)}
.page > *{position:relative;width:626px}
a{text-decoration:none}

/* nav */
.nav{height:32px;background:var(--white)}
.brand{position:absolute;display:flex;align-items:center;gap:3px;font-size:6px;color:var(--navy);letter-spacing:.3px;white-space:nowrap}
.brand i{width:6px;height:6px;background:var(--navy);display:block}
.nav .brand{left:62px;top:13px}
.nav-link{position:absolute;top:12px;font-size:6.5px;line-height:8px;color:var(--ink);white-space:nowrap}
.nav-cta{position:absolute;left:510px;top:7px;width:54px;height:18px;background:var(--navy);color:var(--white);font-size:5.5px;display:flex;align-items:center;justify-content:center}

/* hero */
.hero{height:280px;overflow:hidden}
.hero-photo{position:absolute;inset:0;background:linear-gradient(90deg,#262d66 0%,#2c336c 32%,#56608a 62%,#8d94a8 100%)}
.hero h1{position:absolute;left:83px;top:80px;font-weight:400;font-size:28px;line-height:32px;color:var(--white)}
.hero p{position:absolute;left:83px;top:152px;width:210px;font-size:7px;line-height:11px;color:var(--white)}
.btn{background:var(--green);color:var(--white);font-size:5.5px;display:flex;align-items:center;justify-content:center}
.hero .btn{position:absolute;left:83px;top:182px;width:56px;height:18px}

/* advantages */
.adv{height:183px}
.h2{font-weight:400;font-size:16px;color:var(--ink)}
.adv .h2{position:absolute;left:83px;top:76px}
.adv .sub{position:absolute;left:83px;top:100px;font-size:7px;color:var(--muted)}
.stats{position:absolute;left:343px;top:27px;width:202px;height:130px;display:grid;grid-template-columns:98px 104px;grid-template-rows:65px 65px}
.stat{padding:6px 0 0 0;color:var(--muted)}
.stat:nth-child(2n){border-left:1px solid var(--line);padding-left:7px}
.stat:nth-child(-n+2){border-bottom:1px solid var(--line)}
.stat svg{width:17px;height:17px;display:block}
.stat b{display:block;font-weight:400;font-size:12.5px;line-height:14px;margin-top:10px;color:var(--muted)}
.stat span{display:block;font-size:7px;line-height:9px}

/* services */
.services{height:267px;background:var(--grey-bg)}
.services .h2{position:absolute;left:82px;top:36px}
.cards{position:absolute;left:82px;top:65px;display:flex;gap:11.6px}
.card{width:107px;height:162px;background:var(--white)}
.card-photo{height:78px}
.card h3{font-weight:400;font-size:10.5px;margin:16px 0 0 8px;color:var(--ink)}
.card p{font-size:7px;line-height:11px;margin:5px 8px 0 9px;color:var(--muted)}

/* about / key / featured */
.body{height:918px}
.about-title{position:absolute;left:83px;top:52px;font-weight:400;font-size:16px;line-height:23px}
.about-text{position:absolute;left:83px;top:106px;width:222px;font-size:6.9px;line-height:11.5px;color:var(--muted)}
.about-photo{position:absolute;left:314px;top:52px;width:231px;height:130px}
.key-title{position:absolute;left:0;right:0;top:221px;text-align:center;font-weight:400;font-size:16px}
.key{position:absolute;left:82px;top:279px;width:463px;display:grid;grid-template-columns:repeat(5,1fr);grid-template-rows:72px 80px}
.key div{display:flex;flex-direction:column;align-items:center;padding-top:6px;text-align:center;font-size:7px;line-height:10.5px;color:var(--muted)}
.key div:nth-child(-n+5){border-bottom:1px solid var(--line)}
.key div:not(:nth-child(5n+1)){border-left:1px solid var(--line)}
.key div:nth-child(n+6){padding-top:12px}
.key svg{width:20px;height:22px;margin-bottom:10px;stroke:var(--muted);fill:none;stroke-width:1.2}
.feat-title{position:absolute;left:85px;top:490px;font-weight:400;font-size:16px}
.proj{position:absolute}
.view{position:absolute;left:290px;top:857px;width:45px;height:17px}

/* testimonials */
.testi{height:292px;background:var(--navy)}
.eyebrow{position:absolute;left:0;right:0;top:42px;text-align:center;font-size:7.5px;color:var(--green);letter-spacing:.2px}
.eyebrow:before,.eyebrow:after{content:"";display:inline-block;width:15px;height:1px;background:var(--green);vertical-align:middle;margin:0 5px}
.testi h2{position:absolute;left:0;right:0;top:68px;text-align:center;font-weight:400;font-size:15px;line-height:21px;color:var(--white)}
.quotes{position:absolute;left:86px;top:141px;display:flex;gap:10px}
.quote{width:145px;position:relative}
.bubble{height:58px;background:var(--bubble);color:#e9ecf6;font-size:6.2px;line-height:9px;padding:10px 10px 0 10px;position:relative}
.bubble:after{content:"";position:absolute;left:14px;bottom:-6px;border-left:6px solid transparent;border-top:6px solid var(--bubble)}
.who{display:flex;align-items:center;gap:6px;margin:8px 0 0 10px}
.who .av{width:22px;height:22px;border-radius:50%;background:linear-gradient(135deg,#c9b8a8,#7d6f6a)}
.who b{display:block;font-weight:400;font-size:7.5px;line-height:9px;color:var(--green)}
.who span{display:block;font-size:5.5px;line-height:7px;color:#aeb5d3}

/* contact */
.contact{height:110px;background:var(--sky)}
.contact .h2{position:absolute;left:82px;top:46px;letter-spacing:.4px}
.contact-info{position:absolute;left:393px;top:29px;font-size:7px;line-height:11.5px;color:var(--muted)}
.contact-info strong{display:block;font-weight:400;color:var(--ink);margin-bottom:6px}

/* footer */
.foot{height:117px;background:var(--navy);color:#aab1d2}
.fcol{position:absolute;top:28px;font-size:5px;line-height:11.5px}
.fcol h4{font-weight:400;font-size:6.5px;color:var(--white);margin-bottom:9px}
.fcol p{line-height:7.5px}
.sub-form{display:flex;margin-top:8px}
.sub-form span{width:93px;height:17px;background:var(--white);color:#8a90aa;font-size:4.5px;display:flex;align-items:center;padding-left:12px}
.sub-form i{width:28px;height:17px;background:#1f4fd8;margin-left:5px;display:flex;align-items:center;justify-content:center}

.bar{height:32px;background:var(--bar)}
.bar .brand{left:87px;top:13px}
.copy{position:absolute;left:0;right:0;top:13px;text-align:center;font-size:4.5px;color:var(--green)}
.social{position:absolute;left:472px;top:10px;display:flex;gap:5.3px}
.social i{display:block;width:10.5px;height:10.5px;background:var(--navy)}
</style>
</head>
<body>
<div class="page">

  <header class="nav">
    <div class="brand"><i></i>LARKSPUR</div>
    <a class="nav-link" style="left:143px">Home</a>
    <a class="nav-link" style="left:215px">About</a>
    <a class="nav-link" style="left:279px">Services ⌄</a>
    <a class="nav-link" style="left:347px">Competencies ⌄</a>
    <a class="nav-link" style="left:434px">Contact</a>
    <a class="nav-cta">Contact Us</a>
  </header>

  <section class="hero">
    <div class="hero-photo" role="img" aria-label="Two engineers in hard hats reviewing plans on a steel-framed construction site"></div>
    <h1>Provide Effective<br>Building Solutions</h1>
    <p>Veteran Owned. Ante facilisi convallis phasellus aenean ultrices primis venenatis. Fusce elementum.</p>
    <a class="btn">Get Started</a>
  </section>

  <section class="adv">
    <h2 class="h2">Our Advantages</h2>
    <div class="sub">We're Professional, We're Experienced</div>
    <div class="stats">
      <div class="stat"><svg viewBox="0 0 18 18" fill="none" stroke="#4d5a9a" stroke-width="1"><rect x="2" y="2" width="14" height="14"/><path d="M2 6h14M5 9h8M5 12h8"/></svg><b>128</b><span>Satisfy Client</span></div>
      <div class="stat"><svg viewBox="0 0 18 18" fill="none" stroke="#4d5a9a" stroke-width="1"><path d="M1 3h5l3 4-3 4H1zM7 3h4l3 4"/><circle cx="14" cy="13" r="3"/></svg><b>98</b><span>Project Done</span></div>
      <div class="stat"><svg viewBox="0 0 18 18" fill="none" stroke="#4d5a9a" stroke-width="1"><rect x="2" y="3" width="6" height="12" rx="2"/><rect x="10" y="3" width="6" height="12" rx="2"/></svg><b>34</b><span>Vendor Relation</span></div>
      <div class="stat"><svg viewBox="0 0 18 18" fill="none" stroke="#4d5a9a" stroke-width="1"><path d="M5 2h8v5a4 4 0 0 1-8 0zM9 11v4M6 16h6M5 4H2a3 3 0 0 0 3 4M13 4h3a3 3 0 0 1-3 4"/></svg><b>27</b><span>Professional Award</span></div>
    </div>
  </section>

  <section class="services">
    <h2 class="h2">Our Services</h2>
    <div class="cards">
      <div class="card"><div class="card-photo" role="img" aria-label="Workers in safety vests reviewing drawings outdoors" style="background:linear-gradient(135deg,#5d6b4a,#c9d64a)"></div><h3>Service One</h3><p>Lorem Ipsum is simply dummy text printing and typesetting industry.</p></div>
      <div class="card"><div class="card-photo" role="img" aria-label="Construction crew discussing plans at a brick site" style="background:linear-gradient(135deg,#7a4a3a,#c9a58a)"></div><h3>Service Two</h3><p>Lorem Ipsum is simply dummy text printing and typesetting industry.</p></div>
      <div class="card"><div class="card-photo" role="img" aria-label="Diverse team of builders in hard hats" style="background:linear-gradient(135deg,#8a3a30,#d9c23a)"></div><h3>Service Three</h3><p>Lorem Ipsum is simply dummy text printing and typesetting industry.</p></div>
      <div class="card"><div class="card-photo" role="img" aria-label="Construction crew standing in a row" style="background:linear-gradient(135deg,#4a4f5a,#b8cc40)"></div><h3>Service Four</h3><p>Lorem Ipsum is simply dummy text printing and typesetting industry.</p></div>
    </div>
  </section>

  <section class="body">
    <h2 class="about-title">About Larkspur<br>Site Services LLC</h2>
    <p class="about-text">Larkspur Site Services, LLC [LSS LLC] is a veteran-owned business, and is a leading force in the construction industry. We have continuously provided exceptional services to our clients. With a wealth of experience and a commitment of excellence, we have earned a reputation for delivering high-quality projects on time and within budget.</p>
    <div class="about-photo" role="img" aria-label="Two engineers in safety vests reviewing plans on a tablet" style="background:linear-gradient(135deg,#4e5e3c,#c8d648 60%,#e6e8ea)"></div>

    <h2 class="key-title">Key Services</h2>
    <div class="key">
      <div><svg viewBox="0 0 20 22"><path d="M4 3h12v3H4zM8 6v14h4V6M6 20h8"/></svg>General<br>Contracting</div>
      <div><svg viewBox="0 0 20 22"><rect x="2" y="4" width="14" height="13"/><path d="M2 8h14M6 2v4M12 2v4"/><circle cx="15" cy="17" r="3"/></svg>Construction<br>Management</div>
      <div><svg viewBox="0 0 20 22"><rect x="2" y="3" width="16" height="16"/><path d="M2 8h16M2 13h16M8 3v5M12 8v5M8 13v6"/></svg>Design-Build<br>Services</div>
      <div><svg viewBox="0 0 20 22"><path d="M3 15 15 3l3 3L6 18zM3 4l4 4M12 14l4 4"/></svg>Pre-construction<br>Planning</div>
      <div><svg viewBox="0 0 20 22"><path d="M6 2v5a4 4 0 0 0 8 0V2M10 11v9"/></svg>Value<br>Engineering</div>
      <div><svg viewBox="0 0 20 22"><path d="M4 4h12v16H4zM10 4v16M7 2h6"/></svg>Sustainable<br>Construction Practices</div>
      <div><svg viewBox="0 0 20 22"><path d="M3 4h10v6H3zM7 10v9h3v-9M13 6h5"/></svg>Renovation and<br>Remodeling</div>
      <div><svg viewBox="0 0 20 22"><circle cx="9" cy="7" r="4"/><path d="M2 20a7 7 0 0 1 12-5M15 13l3 1v3c0 2-3 3-3 3s-3-1-3-3v-3z"/></svg>Quality Assurance and<br>Control</div>
      <div><svg viewBox="0 0 20 22"><path d="M3 3v16h16zM7 12v3h3"/></svg>Project Estimating<br>and Budgeting</div>
      <div><svg viewBox="0 0 20 22"><rect x="6" y="2" width="11" height="16"/><path d="M2 9h7M2 13h6M10 6h4"/></svg>Permitting and<br>Regulatory Compliance</div>
    </div>

    <h2 class="feat-title">Featured Projects</h2>
    <div class="proj" role="img" aria-label="Curved glass office building" style="left:82px;top:524px;width:120px;height:150px;background:linear-gradient(160deg,#3f7fc4,#6c8a7a 60%,#2e3a30)"></div>
    <div class="proj" role="img" aria-label="White apartment block under blue sky" style="left:212px;top:524px;width:120px;height:150px;background:linear-gradient(160deg,#3d74c9,#e2e4e6 55%,#5d7a3a)"></div>
    <div class="proj" role="img" aria-label="Glass high-rise facade against sky" style="left:342px;top:524px;width:202px;height:150px;background:linear-gradient(150deg,#b8d8ee,#8fb6d6 45%,#3e5a6a)"></div>
    <div class="proj" role="img" aria-label="Brick federal office building with trees" style="left:82px;top:686px;width:200px;height:149px;background:linear-gradient(180deg,#cfd6e0,#8a6656 45%,#5a5a4a)"></div>
    <div class="proj" role="img" aria-label="Grey concrete architectural fins" style="left:295px;top:686px;width:119px;height:149px;background:linear-gradient(120deg,#e4e4e6,#8b8e95 50%,#4a4c52)"></div>
    <div class="proj" role="img" aria-label="City towers lit at dusk" style="left:426px;top:686px;width:119px;height:149px;background:linear-gradient(180deg,#284e7a,#c69a4e 60%,#3a3a3a)"></div>
    <a class="btn view">View All</a>
  </section>

  <section class="testi">
    <div class="eyebrow">WHAT PEOPLE ARE SAYING</div>
    <h2>What our valuable<br>customer are saying about us?</h2>
    <div class="quotes">
      <div class="quote"><div class="bubble">Rhoncus erat mattis nisl quisque a pellentesque hendrerit eleifend, cras ultrices pretium netus parturient in suscipit mus oyemus jaya komre.</div><div class="who"><div class="av" role="img" aria-label="Customer portrait"></div><div><b>Marco Delacroix</b><span>Customer</span></div></div></div>
      <div class="quote"><div class="bubble">Rhoncus erat mattis nisl quisque a pellentesque hendrerit eleifend, cras ultrices pretium netus parturient in suscipit mus oyemus jaya komre.</div><div class="who"><div class="av" role="img" aria-label="Customer portrait"></div><div><b>Owen Fairbank</b><span>Customer</span></div></div></div>
      <div class="quote"><div class="bubble">Rhoncus erat mattis nisl quisque a pellentesque hendrerit eleifend, cras ultrices pretium netus parturient in suscipit mus oyemus jaya komre.</div><div class="who"><div class="av" role="img" aria-label="Customer portrait"></div><div><b>Lena Whitcombe</b><span>Customer</span></div></div></div>
    </div>
  </section>

  <section class="contact">
    <h2 class="h2">CONTACT INFORMATION</h2>
    <div class="contact-info">
      <strong>Get in touch with our team</strong>
      Dominic Harlowe, President<br>Email Address [TBD]<br>Website Address [TBD]<br>555.214.6730
    </div>
  </section>

  <footer class="foot">
    <div class="fcol" style="left:81px;width:95px"><h4>About company</h4><p>We plan, build and manage sites for federal and commercial clients with care, safety and steady delivery on every single job.</p></div>
    <div class="fcol" style="left:222px"><h4>Company</h4>Overview<br>Preconstruction<br>Construction<br>Design-Build</div>
    <div class="fcol" style="left:316px"><h4>Sectors</h4>Commercial<br>Educational<br>Industrial<br>Senior Living</div>
    <div class="fcol" style="left:410px"><h4>Subscribe to newsletter</h4><p>Enter your email address for<br>receiving valuable newsletters.</p>
      <div class="sub-form"><span>Enter your email Address</span><i><svg width="8" height="6" viewBox="0 0 8 6" fill="none" stroke="#fff" stroke-width=".8"><rect x=".5" y=".5" width="7" height="5"/><path d="M.5.5 4 3.5 7.5.5"/></svg></i></div>
    </div>
  </footer>

  <div class="bar">
    <div class="brand"><i></i>LARKSPUR</div>
    <div class="copy">© 2024 Larkspur Site Services</div>
    <div class="social"><i></i><i></i><i></i><i></i><i></i></div>
  </div>

</div>
</body>
</html>
```